Retirement Plan Advisor Bio

See the attached document and photo for content. I would like someone to design this one page flyer using my logo. This logo was designed by a designer with sketch hive. I am looking for a professional looking document. I want to he color scheme to be primarily white and gold.

Target Market(s)

Employers who offer a retirement plan

Requirements
Should not have
• The designs that I have received look more like resumes. I am interested in advertising my Retirement plan services. If anyone can change their submissions and change it to an ad for retirement plan services instead of a Bio or resume, I would prefer that.

```html
<!DOCTYPE html>
<html lang="en">
<head>
<meta charset="utf-8">
<title>Qualified Professional Retirement Plan Advisor</title>
<link href="https://fonts.googleapis.com/css2?family=Montserrat:wght@400;500;600;700&display=swap" rel="stylesheet">
<style>
  :root {
    --gold: #a6813f;
    --ink: #111111;
    --text: #2b2b2b;
    --white: #ffffff;
    --footer-bg: #f2f2f2;
    --photo-top: #5d6a7e;
    --photo-mid: #c9a77d;
    --photo-low: #2a2522;
  }
  * { box-sizing: border-box; margin: 0; padding: 0; }
  html, body { width: 846px; height: 1200px; overflow: hidden; background: var(--white); }
  body { font-family: "Montserrat", sans-serif; color: var(--text); }
  .flyer { position: relative; width: 846px; height: 1200px; background: var(--white); }

  .portrait {
    position: absolute; left: 0; top: 0; width: 423px; height: 619px;
    background: linear-gradient(170deg, var(--photo-top) 0%, #8a8a86 25%, var(--photo-mid) 50%, #b88d6c 72%, var(--photo-low) 100%);
  }

  .brand-bar {
    position: absolute; left: 423px; top: 0; width: 423px; height: 121px;
    background: var(--gold); display: flex; align-items: center; padding-left: 68px; gap: 10px;
  }
  .brand-bar .mark { width: 12px; height: 12px; background: var(--white); }
  .brand-bar .brand-name { color: var(--white); font-weight: 500; font-size: 19px; letter-spacing: .3px; }

  .headline {
    position: absolute; left: 490px; top: 164px; color: var(--gold);
    font-weight: 700; font-size: 41px; line-height: 48.5px;
  }
  .mission {
    position: absolute; left: 494px; top: 382px; width: 270px;
    font-size: 16.5px; line-height: 22.2px; color: var(--ink); letter-spacing: .2px;
  }
  .mission strong { font-weight: 700; text-decoration: underline; text-underline-offset: 3px; }

  .name-band {
    position: absolute; left: 0; top: 619px; width: 846px; height: 72px;
    background: var(--gold); color: var(--white); text-align: center; padding-right: 28px; padding-top: 10px;
  }
  .name-band h1 { font-size: 25px; font-weight: 700; line-height: 30px; }
  .name-band p { font-size: 13.5px; font-weight: 500; line-height: 18px; }

  .section-title { position: absolute; font-size: 20px; font-weight: 600; color: var(--ink); }
  .list { position: absolute; list-style: none; font-size: 13.3px; line-height: 16px; color: var(--text); letter-spacing: .2px; }
  .list li { position: relative; padding-left: 17px; }
  .list li::before {
    content: ""; position: absolute; left: 0; top: 5px; width: 6px; height: 6px; border-radius: 50%; background: var(--gold);
  }
  .specialties-title { left: 70px; top: 733px; }
  .specialties { left: 84px; top: 772px; width: 340px; }
  .specialties li { margin-bottom: 8px; }
  .qualifications-title { left: 475px; top: 733px; }
  .qualifications { left: 487px; top: 772px; width: 300px; }
  .qualifications li { margin-bottom: 4px; }

  .service-title { position: absolute; left: 70px; top: 953px; font-size: 24px; font-weight: 700; color: var(--gold); }
  .service-copy { position: absolute; left: 72px; top: 991px; width: 360px; font-size: 16.5px; line-height: 19.5px; font-weight: 700; color: #333; }

  .education-title { left: 476px; top: 936px; }
  .education { position: absolute; left: 476px; top: 974px; font-size: 13px; letter-spacing: .2px; }
  .disclaimer { position: absolute; left: 476px; top: 1005px; width: 270px; font-size: 9.6px; line-height: 12px; }

  .footer {
    position: absolute; left: 0; top: 1105px; width: 846px; height: 95px; background: var(--footer-bg);
    font-size: 12.3px; line-height: 14.5px; color: var(--ink); letter-spacing: .2px;
  }
  .contact { position: absolute; top: 33px; display: flex; gap: 5px; }
  .contact svg { width: 11px; height: 11px; flex: none; margin-top: 2px; fill: var(--ink); }
  .contact-name { left: 47px; }
  .contact-address { left: 267px; }
  .contact-phone { left: 451px; flex-direction: column; gap: 0; }
  .contact-phone .row { display: flex; gap: 5px; }
  .contact-web { left: 647px; }
</style>
</head>
<body>
<main class="flyer">
  <div class="portrait" role="img" aria-label="Portrait photograph of the advisor"></div>

  <header class="brand-bar">
    <span class="mark"></span>
    <span class="brand-name">Evenkeel Financial, LLC</span>
  </header>

  <h2 class="headline">Qualified<br>Professional<br>Retirement<br>Plan Advisor</h2>

  <p class="mission">I strive <strong>to improve retirement outcomes</strong> for my plan sponsor clients and their employees through careful retirement plan design assistance, strategic and targeted communication and education, as well as <strong>continual monitoring of results.</strong></p>

  <section class="name-band">
    <h1>Helen R Castell CFP® AIF®</h1>
    <p>Northgate Advisory Advisor</p>
  </section>

  <h3 class="section-title specialties-title">Professional Specialties</h3>
  <ul class="list specialties">
    <li>Over 18 years of experience in the retirement plan industry.</li>
    <li>Focused on helping plan sponsors reduce administrative burdens and fiduciary risk.</li>
    <li>Dedicated to helping employees work toward a positive retirement outcome through careful analysis of their savings rate, investment strategy and overall financial wellness..</li>
  </ul>

  <h3 class="section-title qualifications-title">Qualifications</h3>
  <ul class="list qualifications">
    <li>Certified Financial Planner®</li>
    <li>Accredited Investment Fiduciary®</li>
    <li>Investment Advisor Representative</li>
    <li>Series 7, 63, and 65 Securities licenses with Northgate Advisory</li>
    <li>Holds Life and Health Insurance licenses from Illinois</li>
  </ul>

  <h3 class="service-title">Retirement Plan Advisor</h3>
  <p class="service-copy">Excepteur sint occaecat cupidatat non proident, sunt in culpa qui officia deserunt mollit anim id est laborum.</p>

  <h3 class="section-title education-title">Education</h3>
  <p class="education">BS Marlow Ridge University, 1987</p>
  <p class="disclaimer">*Securities and Investment Advisory Services offered through Northgate Advisory Holdings, Inc. a Registered Broker/Dealer and Investment Advisor, member NBRA/IPSC</p>

  <footer class="footer">
    <div class="contact contact-name">
      <svg viewBox="0 0 12 12"><circle cx="6" cy="3.5" r="3"/><path d="M0 12c0-3.5 2.5-5 6-5s6 1.5 6 5z"/></svg>
      <span>Helen R Castell CFP®AIF®<br>Northgate Advisory Advisor</span>
    </div>
    <div class="contact contact-address">
      <svg viewBox="0 0 12 12"><path d="M6 0a4.2 4.2 0 0 0-4.2 4.2C1.8 7.3 6 12 6 12s4.2-4.7 4.2-7.8A4.2 4.2 0 0 0 6 0zm0 6a1.8 1.8 0 1 1 0-3.6A1.8 1.8 0 0 1 6 6z"/></svg>
      <span>250 Harwick Rd.<br>Fairview, IL 60499</span>
    </div>
    <div class="contact contact-phone">
      <div class="row">
        <svg viewBox="0 0 12 12"><path d="M3 0h6a1 1 0 0 1 1 1v10a1 1 0 0 1-1 1H3a1 1 0 0 1-1-1V1a1 1 0 0 1 1-1zm.5 1.5v8h5v-8z"/></svg>
        <span>(555) 014 2286</span>
      </div>
      <div class="row"><span style="font-weight:600">@</span><span>helen.castell@northgate.example</span></div>
    </div>
    <div class="contact contact-web">
      <svg viewBox="0 0 12 12"><circle cx="6" cy="6" r="5.2" fill="none" stroke="#111" stroke-width="1.4"/><path d="M1 6h10M6 1c-2 2.5-2 7.5 0 10M6 1c2 2.5 2 7.5 0 10" fill="none" stroke="#111" stroke-width="1"/></svg>
      <span>www.helencastell.example</span>
    </div>
  </footer>
</main>
</body>
</html>
```